Stationary & Business Card for Talvo Co, LLC
Talvo Co, LLC
Professional
Adrian Pellworth, MD
President
2918 Larkfield Ave., Suite C-240
Bethesda, MD 20846
dradrian@talvocollc.com
www.talvocollc.com
Our tagline is Your Partner in Personalized Healthcare.
We would like a solid color for our back - either matching the purple or gold of our logo

```html
<!DOCTYPE html>
<html lang="en">
<head>
<meta charset="utf-8">
<title>Talvo Co, LLC — Business Card</title>
<link href="https://fonts.googleapis.com/css2?family=Open+Sans:wght@400;600&display=swap" rel="stylesheet">
<style>
  :root {
    --bg: #e9e7e4;
    --paper: #ffffff;
    --purple: #4b2466;
    --purple-deep: #3a1a52;
    --gold: #e3a624;
    --gold-light: #f0bd3c;
    --ink-light: #ffffff;
  }
  html, body {
    margin: 0;
    width: 1200px;
    height: 901px;
    overflow: hidden;
    background: var(--bg);
    font-family: "Open Sans", Arial, sans-serif;
  }
  .card {
    position: absolute;
    left: 75px;
    top: 150px;
    width: 1050px;
    height: 600px;
    background: var(--paper);
    box-shadow: 0 10px 30px rgba(0,0,0,0.18);
    overflow: hidden;
  }
  .card-shapes { position: absolute; inset: 0; }
  .brand {
    position: absolute;
    left: 48px;
    top: 78px;
    display: flex;
    align-items: center;
    gap: 18px;
  }
  .brand-mark {
    width: 84px;
    height: 84px;
    border-radius: 50%;
    background: var(--purple);
  }
  .brand-name {
    margin: 0;
    font-size: 46px;
    font-weight: 600;
    color: var(--purple);
    letter-spacing: 0.5px;
    line-height: 1;
  }
  .brand-tagline {
    margin: 8px 0 0;
    font-size: 12px;
    color: var(--gold);
    letter-spacing: 1px;
  }
  .holder {
    position: absolute;
    left: 700px;
    top: 272px;
    color: var(--ink-light);
  }
  .holder-name { margin: 0; font-size: 26px; font-weight: 600; }
  .holder-title { margin: 6px 0 0 120px; font-size: 17px; }
  .contact-list {
    position: absolute;
    left: 40px;
    top: 318px;
    margin: 0;
    padding: 0;
    list-style: none;
    color: var(--ink-light);
    font-size: 14px;
    line-height: 1.25;
  }
  .contact-list li {
    display: flex;
    align-items: flex-start;
    gap: 10px;
    margin-bottom: 9px;
  }
  .contact-icon { flex: none; width: 16px; height: 16px; margin-top: 1px; }
  .web-address {
    position: absolute;
    right: 60px;
    top: 452px;
    margin: 0;
    font-size: 18px;
    letter-spacing: 7px;
    color: var(--purple-deep);
  }
</style>
</head>
<body>
<div class="card">
  <svg class="card-shapes" viewBox="0 0 1050 600" width="1050" height="600" aria-hidden="true">
    <path d="M0,238 L748,238 L770,218 L792,238 L1050,238 L1050,600 L0,600 Z" fill="var(--purple)"/>
    <path d="M0,572 C300,578 450,560 560,476 C640,414 720,398 1050,398 L1050,600 L0,600 Z" fill="var(--gold)"/>
    <path d="M0,572 C300,578 450,560 560,476 C640,414 720,398 1050,398" fill="none" stroke="var(--gold-light)" stroke-width="4"/>
  </svg>

  <div class="brand">
    <div class="brand-mark"></div>
    <div>
      <p class="brand-name">Talvo Co, LLC</p>
      <p class="brand-tagline">Your Partner in Personalized Healthcare</p>
    </div>
  </div>

  <div class="holder">
    <p class="holder-name">Adrian Pellworth, MD</p>
    <p class="holder-title">President</p>
  </div>

  <ul class="contact-list">
    <li>
      <svg class="contact-icon" viewBox="0 0 16 16"><circle cx="8" cy="8" r="8" fill="#fff"/><path d="M8 3.5a3 3 0 0 0-3 3c0 2.2 3 6 3 6s3-3.8 3-6a3 3 0 0 0-3-3zm0 4.2a1.2 1.2 0 1 1 0-2.4 1.2 1.2 0 0 1 0 2.4z" fill="var(--purple)"/></svg>
      <span>2918 Larkfield Ave., Suite C-240<br>Bethesda, MD 20846</span>
    </li>
    <li>
      <svg class="contact-icon" viewBox="0 0 16 16"><circle cx="8" cy="8" r="8" fill="#fff"/><path d="M5.2 4h1.6l.8 2-1 .8a5 5 0 0 0 2.6 2.6l.8-1 2 .8v1.6c0 .4-.3.7-.7.7A7.3 7.3 0 0 1 4.5 4.7c0-.4.3-.7.7-.7z" fill="var(--purple)"/></svg>
      <span>(240) 555-0142</span>
    </li>
    <li>
      <svg class="contact-icon" viewBox="0 0 16 16"><circle cx="8" cy="8" r="8" fill="#fff"/><rect x="4.5" y="6" width="7" height="5" fill="var(--purple)"/><rect x="5.5" y="4" width="5" height="2" fill="var(--purple)"/></svg>
      <span>(240) 555-0187</span>
    </li>
    <li>
      <svg class="contact-icon" viewBox="0 0 16 16"><circle cx="8" cy="8" r="8" fill="#fff"/><rect x="4" y="5" width="8" height="6" fill="var(--purple)"/><path d="M4 5l4 3.2L12 5" fill="none" stroke="#fff" stroke-width="0.9"/></svg>
      <span>dradrian@talvocollc.com</span>
    </li>
    <li>
      <svg class="contact-icon" viewBox="0 0 16 16"><circle cx="8" cy="8" r="8" fill="#fff"/><circle cx="8" cy="8" r="4" fill="none" stroke="var(--purple)" stroke-width="1.2"/><path d="M4 8h8M8 4c-2 2.4-2 5.6 0 8M8 4c2 2.4 2 5.6 0 8" fill="none" stroke="var(--purple)" stroke-width="0.9"/></svg>
      <span>www.talvocollc.com</span>
    </li>
  </ul>

  <p class="web-address">www.talvocollc.com</p>
</div>
</body>
</html>
```